Redesign for existing homepage

We would like a redesign for our websites 2 column homepage
We provide engine repair and reconditioning services
We would like a cleaner, modern site that works well with our logo colors
Please see the attached brief for more info
Target Market(s)
25 - 45
Industry/Entity Type
Cleaner
Requirements
Must have
- Google Fonts

```html
<!DOCTYPE html>
<html lang="en">
<head>
<meta charset="utf-8">
<title>Harlow Engine Works</title>
<link href="https://fonts.googleapis.com/css2?family=Open+Sans:wght@400;600;700&family=Arimo:wght@400;700&display=swap" rel="stylesheet">
<style>
:root{
  --yellow:#fdc100;
  --yellow-deep:#f2b400;
  --nav:#2b2b2b;
  --nav-line:#444;
  --panel:#545454;
  --text:#6b6b6b;
  --heading:#222;
  --blue:#0047d6;
  --white:#fff;
}
*{margin:0;padding:0;box-sizing:border-box}
html,body{width:949px;height:1200px;overflow:hidden;background:#fff}
body{position:relative;font-family:"Open Sans",sans-serif;color:var(--text)}
.abs{position:absolute}

/* header */
.header{left:136px;top:20px;width:678px;height:132px;background:var(--yellow)}
.tagline{left:30px;top:60px;color:var(--white);font-size:9.5px;font-weight:600;line-height:16px;text-transform:uppercase}
.brand{left:270px;top:32px;width:144px;height:70px;display:flex;align-items:center;justify-content:center;gap:8px}
.brand-dot{width:14px;height:14px;border-radius:50%;background:var(--blue)}
.brand-name{font-family:"Open Sans",sans-serif;font-weight:700;font-size:15px;color:var(--blue);line-height:17px;text-align:left}
.phone-ico{left:504px;top:56px}
.call{left:554px;top:52px;color:var(--white);font-family:"Arimo",sans-serif;font-size:13.5px;line-height:21px}
.call b{font-weight:700}

/* nav */
.nav{left:136px;top:152px;width:678px;height:38px;background:var(--nav);display:flex;align-items:center}
.nav .home{width:42px;height:38px;display:flex;align-items:center;justify-content:center;border-right:1px solid var(--nav-line)}
.nav a{color:var(--white);text-decoration:none;font-size:9.4px;font-weight:600;text-transform:uppercase;height:38px;display:flex;align-items:center;justify-content:center;border-right:1px solid var(--nav-line)}
.nav a:last-child{border-right:0}

/* hero */
.hero{left:136px;top:190px;width:678px;height:316px;background:radial-gradient(ellipse at 60% 40%,#8a8178 0%,#5a5550 45%,#2e2c2a 100%)}
.caption{left:136px;top:306px}
.caption-text{left:150px;top:322px;color:var(--white);font-family:"Arimo",sans-serif;font-weight:700;font-size:16px;line-height:30px}
.arrow{width:37px;height:36px;border:1px solid rgba(255,255,255,.85);top:406px;display:flex;align-items:center;justify-content:center}

/* welcome */
.welcome{left:136px;top:524px;width:434px}
.welcome h1{font-weight:400;font-size:17.5px;color:var(--heading);padding-bottom:6px;border-bottom:1px solid #e3e3e3}
.welcome h1 span{color:var(--yellow)}
.welcome p{font-size:9.3px;line-height:16.3px;text-align:justify;margin-top:8px}
.welcome p+p{margin-top:16px}
.welcome ul{list-style:none;margin-top:9px;font-family:"Arimo",sans-serif;font-size:10px}
.welcome li{height:21.6px;padding-left:15px;position:relative}
.welcome li::before{content:"›";position:absolute;left:0;top:-1px;font-size:11px}

/* enquiry */
.enquiry{left:602px;top:525px;width:212px;height:273px;background:var(--panel);border-radius:2px}
.enquiry h2{font-family:"Arimo",sans-serif;font-weight:400;font-size:12px;color:#eee;padding:9px 14px 6px;border-bottom:1px dashed #7a7a7a}
.field{position:absolute;left:12px;display:flex;color:var(--white);font-family:"Arimo",sans-serif;font-size:9.8px}
.field label{width:65px;padding-top:6px}
.field .input{width:116px;height:25px;background:#fafafa;border:1px solid #ddd;border-radius:2px;color:#666;font-size:8px;padding:7px 10px}
.submit{left:75px;top:234px;width:67px;height:29px;background:#3f3f3f;border:1px solid #2e2e2e;border-radius:3px;color:var(--white);font-size:12.5px;display:flex;align-items:center;justify-content:center}

/* features */
.feature{top:842px;width:212px}
.feature .photo{height:136px}
.feature h3{font-weight:400;font-size:12.6px;line-height:17px;color:#555;margin-top:13px}
.feature p{font-size:8.8px;line-height:15.2px;text-align:justify;margin-top:9px;color:#7a7a7a}
.btn{display:inline-flex;align-items:center;justify-content:center;width:96px;height:26px;background:var(--yellow);color:var(--white);font-size:10px;font-weight:600;margin-top:12px}

/* footer */
.footer{left:136px;top:1131px;width:678px;height:51px;background:var(--blue);color:var(--white);font-family:"Arimo",sans-serif;font-size:8px}
.copy{left:14px;top:21px}
.social{top:13px;width:24px;height:24px;border-radius:50%;border:1px solid rgba(255,255,255,.35)}
.badge-a{left:352px;top:12px;width:24px;height:27px;background:var(--yellow);border-radius:2px}
.badge-b{left:384px;top:12px;width:48px;height:27px;background:#111;border-radius:50%}
.links{right:12px;top:21px;word-spacing:2px}
</style>
</head>
<body>

<header class="header abs">
  <div class="tagline abs">Engine repairs and<br>reconditioning specialists</div>
  <div class="brand abs"><span class="brand-dot"></span><span class="brand-name">Harlow<br>Engine Works</span></div>
  <svg class="phone-ico abs" width="32" height="32" viewBox="0 0 32 32" aria-hidden="true">
    <circle cx="16" cy="16" r="15" fill="none" stroke="#f7d25a" stroke-width="1"/>
    <path d="M9 13c0-2 3-3 7-3s7 1 7 3v1h-3v-1h-8v1H9z M11 15h10l1 7H10z" fill="#fff"/>
    <circle cx="16" cy="18.5" r="1.8" fill="#fdc100"/>
  </svg>
  <div class="call abs">Call us free on<br><b>04 555 0187</b></div>
</header>

<nav class="nav abs">
  <span class="home">
    <svg width="20" height="17" viewBox="0 0 20 17" aria-hidden="true"><path d="M10 1 1 9h3v7h4v-5h4v5h4V9h3z" fill="#fdc100"/></svg>
  </span>
  <a style="width:75px">About Us</a>
  <a style="width:189px">Private Vehicle Service &amp; Repair</a>
  <a style="width:122px">Trade Customers</a>
  <a style="width:165px">Race &amp; Classic Car Engines</a>
  <a style="width:85px">Contact Us</a>
</nav>

<div class="hero abs" role="img" aria-label="Close-up of a mechanic's hand working inside an engine gearbox"></div>
<svg class="caption abs" width="360" height="82" viewBox="0 0 360 82" aria-hidden="true">
  <path d="M0 0H324L358 80H0Z" fill="#f2b400" fill-opacity=".85"/>
  <path d="M0 1H323L357 80" fill="none" stroke="#ffe48a" stroke-width="2"/>
  <path d="M0 80H358" stroke="#ffe48a" stroke-width="2"/>
</svg>
<div class="caption-text abs">Specialist engine repair &amp; reconditioning<br>To have your car running at its best</div>
<div class="arrow abs" style="left:148px"><svg width="12" height="18" viewBox="0 0 12 18"><path d="M10 1 2 9l8 8" fill="none" stroke="#fff" stroke-width="1.5"/></svg></div>
<div class="arrow abs" style="left:189px"><svg width="12" height="18" viewBox="0 0 12 18"><path d="M2 1l8 8-8 8" fill="none" stroke="#fff" stroke-width="1.5"/></svg></div>

<section class="welcome abs">
  <h1>Welcome To <span>HEW</span></h1>
  <p>Lorem ipsu m dolor sit uer scing elitraesentves tibuum molestieum sociis natoqu. Enean nonummy hendre-rit uris. Phasellus porta. Fusce suscipit varius mi. Cum sociis natoque penatibus et magnis dis parturi ent montes</p>
  <p>Jascetur ridiculus mus. Nulla duiuscgiat malesuada odio.Morbi nunc odio , gravida at, cursus nec luctus a lorem. Maecenas tristique orci ac sem. Duis ultricies pharetra magna. Donec accumsan malesuada orci. Donec sit amet eros. Lorem ipsum dolor sit amet, consectetuer adipiscing elit. Mauris fermentum dictum magna. Sed laoreet</p>
  <ul>
    <li>Lorem ipsum dolor sit amet</li>
    <li>Sed in lacus ut enim adipiscing</li>
    <li>Vestibulum iaculis lacinia est</li>
    <li>Vestibulum iaculis lacinia est</li>
    <li>Sed in lacus ut enim adipiscing&nbsp; Sed in lacus ut enim adipiscing</li>
  </ul>
</section>

<aside class="enquiry abs">
  <h2>Make an Enquiry</h2>
  <div class="field" style="top:51px"><label>Name *</label><div class="input">Name</div></div>
  <div class="field" style="top:92px"><label>Address *</label><div class="input">Address</div></div>
  <div class="field" style="top:133px"><label>Phone No *</label><div class="input">Phone</div></div>
  <div class="field" style="top:173px"><label>Message *</label><div class="input" style="height:46px">Message</div></div>
  <div class="submit abs">Submit</div>
</aside>

<article class="feature abs" style="left:136px">
  <div class="photo" role="img" aria-label="Father and son working under the bonnet of a car in a garden" style="background:linear-gradient(135deg,#6f8f4a,#a35a4a 60%,#3a3030)"></div>
  <h3>Need service and repair for a private vehicle?</h3>
  <p>Get an efficient and honest diagnosis, along with repair work that will have your car running smoothly.</p>
  <span class="btn">Make an Enquiry</span>
</article>
<article class="feature abs" style="left:366px">
  <div class="photo" role="img" aria-label="Mechanic and a satisfied customer standing by a car in a workshop" style="background:linear-gradient(135deg,#7c7f86,#9a4036 50%,#d8cfc4)"></div>
  <h3>Interested in becoming a trade customer?</h3>
  <p>Get an efficient and honest diagnosis, along with repair work that will have your car running smoothly.</p>
  <span class="btn">Trade Customers</span>
</article>
<article class="feature abs" style="left:602px">
  <div class="photo" role="img" aria-label="Orange race car parked in a bright workshop" style="background:linear-gradient(160deg,#d9d2c2,#4a4642 45%,#e88a1c 75%,#3a3632)"></div>
  <h3>Is your classic or race car your passion?</h3>
  <p>Get an efficient and honest diagnosis, along with repair work that will have your car running smoothly.</p>
  <span class="btn">Contact Us</span>
</article>

<footer class="footer abs">
  <div class="copy abs">©2014 harlowengines.example , All Rights Reserved.</div>
  <span class="social abs" style="left:229px"></span>
  <span class="social abs" style="left:258px"></span>
  <span class="social abs" style="left:286px"></span>
  <span class="badge-a abs"></span>
  <span class="badge-b abs"></span>
  <div class="links abs">Home &nbsp; | &nbsp; About &nbsp; | Make an Enquiry | Contacts</div>
</footer>

</body>
</html>
```